IT Service Provider

We need a website which reflects the IT Services we can offer to small and mid-size companies. This reaches from LAN/WAN, Security, VoIP, WiFi, Storage, Penetration testing.and Support.

In addition to that, a Logo is needed and should be embedded in the website.

Company is registered in the UK under:
Kovilant Ltd
Company No. 05927318

Industry/Entity Type

Security

```html
<!DOCTYPE html>
<html lang="en">
<head>
<meta charset="utf-8">
<title>Kovilant – IT Services</title>
<link href="https://fonts.googleapis.com/css2?family=Lato:wght@400;700;900&display=swap" rel="stylesheet">
<style>
:root{
  --blue:#1f8fd6;
  --ink:#333a40;
  --muted:#8a9096;
  --line:#e3e6e9;
  --soft:#f1f3f5;
  --dark:#23272c;
  --dark-2:#2d3238;
  --white:#ffffff;
}
*{box-sizing:border-box;margin:0;padding:0}
html,body{width:1200px;height:3240px;overflow:hidden}
body{font-family:'Lato',Arial,sans-serif;color:var(--ink);background:var(--white);font-size:15px;line-height:1.5}
.wrap{width:1080px;margin:0 auto;position:relative}

/* header */
.site-header{height:110px;border-bottom:1px solid var(--line)}
.site-header .wrap{display:flex;align-items:center;justify-content:space-between;height:110px}
.brand{display:flex;align-items:center;gap:14px;font-size:36px;font-weight:700;color:var(--blue);line-height:1}
.brand-mark{width:32px;height:32px;background:var(--blue);flex:none}
.nav{display:flex;gap:6px;list-style:none;font-size:15px}
.nav li{padding:14px 22px;color:var(--ink)}
.nav li.active{border-top:3px solid var(--blue);color:var(--blue);box-shadow:0 2px 8px rgba(0,0,0,.1)}

/* hero */
.hero{height:470px;position:relative;overflow:hidden}
.hero-bg{position:absolute;inset:0;background:linear-gradient(120deg,#6d8ea0 0%,#a9c2cf 45%,#d6e0e6 100%)}
.hero-person{position:absolute;right:130px;bottom:0;width:360px;height:460px;background:linear-gradient(180deg,#3d4a57,#1f262d);border-radius:160px 160px 0 0}
.hero-copy{position:absolute;left:60px;top:90px;width:560px;color:var(--white)}
.hero-copy h1{font-size:46px;font-weight:900;line-height:1.1;text-transform:uppercase}
.hero-copy p{margin-top:16px;font-size:16px;font-weight:700}
.btns{margin-top:30px;display:flex;gap:16px}
.btn{background:var(--blue);color:var(--white);padding:12px 26px;font-size:15px;font-weight:700}
.dots{position:absolute;left:50%;bottom:22px;transform:translateX(-50%);display:flex;gap:8px}
.dots span{width:12px;height:12px;border-radius:50%;background:rgba(255,255,255,.6)}
.dots span.on{background:var(--white)}

/* services */
.services{height:900px;padding-top:60px;background:linear-gradient(180deg,#f4f5f6,#fff 40%)}
.section-title{text-align:center;font-size:30px;font-weight:700}
.section-sub{text-align:center;color:var(--muted);font-size:14px;width:640px;margin:10px auto 0}
.services-body{position:relative;height:700px;margin-top:20px}
.services-person{position:absolute;left:60px;top:40px;width:380px;height:660px;background:linear-gradient(180deg,#2b2f35 0%,#1b1d21 70%,#3a3e44 100%);border-radius:180px 180px 0 0}
.service-rail{position:absolute;left:560px;top:30px;width:2px;height:640px;background:var(--line)}
.service-list{position:absolute;left:530px;top:20px;list-style:none}
.service{display:flex;gap:30px;height:132px}
.service-icon{width:62px;height:62px;border-radius:50%;background:var(--white);border:2px solid var(--line);display:flex;align-items:center;justify-content:center;flex:none}
.service h3{color:var(--blue);font-size:17px;font-weight:700;text-transform:uppercase}
.service p{color:var(--muted);font-size:13px;width:420px;line-height:1.45}
.read{font-size:13px;font-weight:700;color:var(--ink)}

/* events */
.events{height:670px;position:relative;padding-top:60px}
.events-bg{position:absolute;inset:0;background:linear-gradient(135deg,#3a3f45,#1d2024)}
.heading{font-size:28px;font-weight:700}
.heading b{color:var(--blue);font-weight:700}
.events .heading{color:var(--white)}
.heading-rule{width:70px;height:3px;background:var(--blue);margin-top:8px}
.cards{display:flex;gap:30px;margin-top:30px}
.card{width:340px;background:var(--white)}
.card-media{height:150px;background:linear-gradient(135deg,#9aa3ab,#5b646c);position:relative}
.date{position:absolute;left:0;top:0;width:80px;height:90px;background:var(--blue);color:var(--white);text-align:center;padding-top:8px}
.date strong{display:block;font-size:32px;line-height:1}
.date span{font-size:13px;font-weight:700}
.card-body{padding:18px 20px}
.card-body h4{font-size:17px}
.card-body p{font-size:13px;color:var(--muted);margin:8px 0 14px}
.card-body .read{color:var(--blue)}
.card-foot{border-top:1px solid var(--line);padding:12px 20px;font-size:12px;color:var(--muted);display:flex;align-items:center;gap:8px}

/* testimonials */
.testimonials{height:370px;padding-top:50px}
.quotes{display:flex;gap:60px;margin-top:26px}
.quote{width:510px}
.quote-box{background:var(--soft);padding:20px 40px;position:relative;font-size:13px;color:var(--muted)}
.quote-box::before{content:"\201C";position:absolute;left:12px;top:0;font-size:44px;color:#b5bbc1}
.quote-box::after{content:"\201D";position:absolute;right:12px;bottom:-14px;font-size:44px;color:#b5bbc1}
.see{text-align:right;color:var(--blue);font-size:12px;margin-top:4px}
.author{display:flex;align-items:center;gap:20px;margin-top:6px;padding-left:20px}
.avatar{width:70px;height:70px;border-radius:50%;background:linear-gradient(135deg,#c9b8a6,#6f6258)}
.author strong{display:block;font-size:16px}
.author span{font-size:12px;color:var(--muted)}

/* news + video */
.latest{height:470px;border-top:1px solid var(--line);padding-top:40px}
.latest .wrap{display:flex;gap:60px}
.news{width:340px}
.news-item{display:flex;gap:18px;margin-top:24px;padding-bottom:18px;border-bottom:1px solid var(--line)}
.news-date{width:62px;flex:none;text-align:center;border:1px solid var(--line)}
.news-date strong{display:block;font-size:20px;padding-top:4px}
.news-date span{font-size:11px;color:var(--muted)}
.news-date em{display:block;font-style:normal;background:var(--blue);color:var(--white);font-size:12px;font-weight:700;padding:3px 0}
.news-item h5{font-size:14px}
.news-item p{font-size:12px;color:var(--muted)}
.meta{font-size:11px;color:var(--muted);margin-top:6px}
.video{flex:1}
.video-frame{margin-top:24px;height:220px;background:linear-gradient(135deg,#3d6f9a,#b8d2e6 60%,#e8eef3)}
.video-bar{height:36px;background:#2b2f34;display:flex;align-items:center;gap:14px;padding:0 14px}
.track{flex:1;height:4px;background:#555b61;position:relative}
.track i{position:absolute;left:0;top:0;height:4px;width:28%;background:#e0443b}
.vol{width:60px;height:4px;background:#e0443b}
.video h5{font-size:15px;margin-top:14px}
.video p{font-size:12px;color:var(--muted)}

/* footer */
.site-footer{height:250px;background:var(--dark);color:#c9cdd1;padding-top:34px}
.foot-cols{display:flex;justify-content:space-between}
.foot-col h6{color:var(--white);font-size:17px;margin-bottom:12px}
.foot-col li{list-style:none;font-size:12px;line-height:1.7}
.social{display:flex;gap:6px}
.social div{width:70px;text-align:center}
.social .sq{height:56px}
.social .n{background:var(--dark-2);font-size:12px;padding:3px 0;color:var(--white)}
.s1 .sq{background:#3b5a99}.s2 .sq{background:#2aa3d8}.s3 .sq{background:#d2493d}.s4 .sq{background:#5a6470}
.foot-col.links,.foot-col.info,.foot-col.products{border-left:1px solid #3a3f45;padding-left:24px;width:200px}
.copy{text-align:center;font-size:11px;color:#8a9096;margin-top:26px}
</style>
</head>
<body>

<header class="site-header">
  <div class="wrap">
    <div class="brand"><span class="brand-mark"></span>Kovilant</div>
    <ul class="nav">
      <li class="active">Home</li><li>About Us</li><li>Solutions</li><li>Media</li><li>Services</li><li>Contact Us</li>
    </ul>
  </div>
</header>

<section class="hero">
  <div class="hero-bg" role="img" aria-label="Blurred office interior background"></div>
  <div class="hero-person" role="img" aria-label="Businessman in a suit holding a tablet"></div>
  <div class="hero-copy">
    <h1>IT Services Company<br>That You Need!</h1>
    <p>Lorem ipsum dolor sit amet, consectetur adipiscing elit, sed diam nonummy nibh euismod tincidunt ut laoreet.</p>
    <div class="btns"><span class="btn">Learn More</span><span class="btn">Register Now</span></div>
  </div>
  <div class="dots"><span class="on"></span><span></span><span></span><span></span></div>
</section>

<section class="services">
  <h2 class="section-title">IT Services Company Research</h2>
  <p class="section-sub">Lorem ipsum dolor sit amet, consectetur adipiscing elit, sed diam nonummy nibh euismod tincidunt ut laoreet dolore magna aliquam erat volutpat.</p>
  <div class="wrap services-body">
    <div class="services-person" role="img" aria-label="Businesswoman holding a red folder, presenting the services"></div>
    <div class="service-rail"></div>
    <ul class="service-list">
      <li class="service">
        <div class="service-icon"><svg width="30" height="30" viewBox="0 0 30 30"><rect x="3" y="4" width="24" height="16" rx="2" fill="none" stroke="#1f8fd6" stroke-width="2.5"/><rect x="11" y="22" width="8" height="4" fill="#1f8fd6"/></svg></div>
        <div><h3>LAN/WAN Services</h3><p>Lorem ipsum dolor sit amet, consectetur adipiscing elit, sed diam nonummy nibh euismod tincidunt ut laoreet dolore magna aliquam erat volutpat.</p><span class="read">Read More</span></div>
      </li>
      <li class="service">
        <div class="service-icon"><svg width="30" height="30" viewBox="0 0 30 30"><rect x="6" y="13" width="18" height="13" rx="2" fill="#1f8fd6"/><path d="M10 13V9a5 5 0 0 1 10 0v4" fill="none" stroke="#1f8fd6" stroke-width="2.5"/></svg></div>
        <div><h3>Security Services</h3><p>Lorem ipsum dolor sit amet, consectetur adipiscing elit, sed diam nonummy nibh euismod tincidunt ut laoreet dolore magna aliquam erat volutpat.</p><span class="read">Read More</span></div>
      </li>
      <li class="service">
        <div class="service-icon"><svg width="30" height="30" viewBox="0 0 30 30"><path d="M4 12a16 16 0 0 1 22 0M8 16a10 10 0 0 1 14 0M12 20a4 4 0 0 1 6 0" fill="none" stroke="#1f8fd6" stroke-width="2.5"/><circle cx="15" cy="24" r="2" fill="#1f8fd6"/></svg></div>
        <div><h3>WiFi Services</h3><p>Lorem ipsum dolor sit amet, consectetur adipiscing elit, sed diam nonummy nibh euismod tincidunt ut laoreet dolore magna aliquam erat volutpat.</p><span class="read">Read More</span></div>
      </li>
      <li class="service">
        <div class="service-icon"><svg width="30" height="30" viewBox="0 0 30 30"><path d="M8 22a6 6 0 0 1 1-12 8 8 0 0 1 15 3 5 5 0 0 1-1 9z" fill="#1f8fd6"/></svg></div>
        <div><h3>Penetration Testing Services</h3><p>Lorem ipsum dolor sit amet, consectetur adipiscing elit, sed diam nonummy nibh euismod tincidunt ut laoreet dolore magna aliquam erat volutpat.</p><span class="read">Read More</span></div>
      </li>
      <li class="service">
        <div class="service-icon"><svg width="30" height="30" viewBox="0 0 30 30"><circle cx="15" cy="15" r="11" fill="none" stroke="#1f8fd6" stroke-width="2.5"/><path d="M15 8v7l5 3" fill="none" stroke="#1f8fd6" stroke-width="2.5"/></svg></div>
        <div><h3>Support Services</h3><p>Lorem ipsum dolor sit amet, consectetur adipiscing elit, sed diam nonummy nibh euismod tincidunt ut laoreet dolore magna aliquam erat volutpat.</p><span class="read">Read More</span></div>
      </li>
    </ul>
  </div>
</section>

<section class="events">
  <div class="events-bg" role="img" aria-label="Dimmed office photo behind the events"></div>
  <div class="wrap">
    <h2 class="heading"><b>Recent</b> Events</h2>
    <div class="heading-rule"></div>
    <div class="cards">
      <article class="card">
        <div class="card-media" role="img" aria-label="Hands typing on a laptop"><div class="date"><strong>01</strong><span>OCT</span></div></div>
        <div class="card-body"><h4>Sed vel urna vitae tortor</h4><p>Lorem ipsum dolor sit amet, consectetur adipiscing elit. Sed vel urna vitae tortor blandit aliquet. Pellentesque habitant morbi tristique senectus et netus et malesuada fames ac turpis egestas.</p><span class="read">Read More</span></div>
        <div class="card-foot"><svg width="10" height="14" viewBox="0 0 10 14"><path d="M5 0a5 5 0 0 1 5 5c0 4-5 9-5 9S0 9 0 5a5 5 0 0 1 5-5z" fill="#8a9096"/></svg>12 Marlow Yard, London, UK</div>
      </article>
      <article class="card">
        <div class="card-media" role="img" aria-label="Server cables and network hardware"><div class="date"><strong>01</strong><span>OCT</span></div></div>
        <div class="card-body"><h4>Sed vel urna vitae tortor</h4><p>Lorem ipsum dolor sit amet, consectetur adipiscing elit. Sed vel urna vitae tortor blandit aliquet. Pellentesque habitant morbi tristique senectus et netus et malesuada fames ac turpis egestas.</p><span class="read">Read More</span></div>
        <div class="card-foot"><svg width="10" height="14" viewBox="0 0 10 14"><path d="M5 0a5 5 0 0 1 5 5c0 4-5 9-5 9S0 9 0 5a5 5 0 0 1 5-5z" fill="#8a9096"/></svg>12 Marlow Yard, London, UK</div>
      </article>
      <article class="card">
        <div class="card-media" role="img" aria-label="Grey gear wheels with one red gear"><div class="date"><strong>01</strong><span>OCT</span></div></div>
        <div class="card-body"><h4>Sed vel urna vitae tortor</h4><p>Lorem ipsum dolor sit amet, consectetur adipiscing elit. Sed vel urna vitae tortor blandit aliquet. Pellentesque habitant morbi tristique senectus et netus et malesuada fames ac turpis egestas.</p><span class="read">Read More</span></div>
        <div class="card-foot"><svg width="10" height="14" viewBox="0 0 10 14"><path d="M5 0a5 5 0 0 1 5 5c0 4-5 9-5 9S0 9 0 5a5 5 0 0 1 5-5z" fill="#8a9096"/></svg>12 Marlow Yard, London, UK</div>
      </article>
    </div>
  </div>
</section>

<section class="testimonials">
  <div class="wrap">
    <h2 class="heading">Testimonials</h2>
    <div class="heading-rule"></div>
    <div class="quotes">
      <div class="quote">
        <div class="quote-box">Lorem ipsum dolor sit amet, consectetur adipiscing elit, sed diam nonummy nibh euismod tincidunt ut laoreet dolore magna aliquam erat volutpat. Ut wisi enim ad minim veniam, quis nostrud exerci.</div>
        <div class="see">See all reviews</div>
        <div class="author"><div class="avatar" role="img" aria-label="Client portrait"></div><div><strong>Alan Porter</strong><span>IT Manager, UK</span></div></div>
      </div>
      <div class="quote">
        <div class="quote-box">Lorem ipsum dolor sit amet, consectetur adipiscing elit, sed diam nonummy nibh euismod tincidunt ut laoreet dolore magna aliquam erat volutpat. Ut wisi enim ad minim veniam, quis nostrud exerci.</div>
        <div class="see">See all reviews</div>
        <div class="author"><div class="avatar" role="img" aria-label="Client portrait"></div><div><strong>Alan Porter</strong><span>IT Manager, UK</span></div></div>
      </div>
    </div>
  </div>
</section>

<section class="latest">
  <div class="wrap">
    <div class="news">
      <h2 class="heading"><b>Latest</b> News</h2>
      <div class="heading-rule"></div>
      <div class="news-item"><div class="news-date"><strong>01</strong><span>OCT</span><em>2016</em></div><div><h5>Ut wisi enim ad minim veniam</h5><p>Lorem ipsum dolor sit amet, consectetur adipiscing elit sed diam.</p><div class="meta">Alan Porter · 0 Comments</div></div></div>
      <div class="news-item"><div class="news-date"><strong>01</strong><span>OCT</span><em>2016</em></div><div><h5>Ut wisi enim ad minim veniam</h5><p>Lorem ipsum dolor sit amet, consectetur adipiscing elit sed diam.</p><div class="meta">Alan Porter · 0 Comments</div></div></div>
      <div class="news-item"><div class="news-date"><strong>01</strong><span>OCT</span><em>2016</em></div><div><h5>Ut wisi enim ad minim veniam</h5><p>Lorem ipsum dolor sit amet, consectetur adipiscing elit sed diam.</p><div class="meta">Alan Porter · 0 Comments</div></div></div>
    </div>
    <div class="video">
      <h2 class="heading"><b>Latest</b> Video</h2>
      <div class="heading-rule"></div>
      <div class="video-frame" role="img" aria-label="Video still of a business team around a digital network graphic"></div>
      <div class="video-bar">
        <svg width="14" height="16" viewBox="0 0 14 16"><path d="M0 0l14 8-14 8z" fill="#fff"/></svg>
        <div class="track"><i></i></div>
        <svg width="16" height="14" viewBox="0 0 16 14"><path d="M0 4h4l5-4v14l-5-4H0z" fill="#fff"/></svg>
        <div class="vol"></div>
      </div>
      <h5>Duis sapien turpis, tempus nec porta eget</h5>
      <p>Lorem ipsum dolor sit amet, consectetur adipiscing elit. Sed vel urna vitae tortor blandit aliquet, pellentesque habitant morbi tristique senectus et netus.</p>
    </div>
  </div>
</section>

<footer class="site-footer">
  <div class="wrap">
    <div class="foot-cols">
      <div class="foot-col">
        <h6>Follow Us</h6>
        <div class="social">
          <div class="s1"><div class="sq"></div><div class="n">146k</div></div>
          <div class="s2"><div class="sq"></div><div class="n">98k</div></div>
          <div class="s3"><div class="sq"></div><div class="n">124k</div></div>
          <div class="s4"><div class="sq"></div><div class="n">88k</div></div>
        </div>
      </div>
      <div class="foot-col info">
        <h6>Contact Info</h6>
        <ul><li>Kovilant Ltd</li><li>Company No. 05927318</li><li>12 Marlow Yard</li><li>London, UK</li><li>hello@kovilant.example</li></ul>
      </div>
      <div class="foot-col links">
        <h6>Links</h6>
        <ul><li>Knowledge Base</li><li>Jobs</li><li>Press</li><li>Terms of Services</li><li>Privacy Policy</li></ul>
      </div>
      <div class="foot-col products">
        <h6>Products</h6>
        <ul><li>Solutions</li><li>Catalogue</li><li>Comparison</li><li>ISO/PTE Certification</li><li>Broadband Routes</li></ul>
      </div>
    </div>
    <p class="copy">Copyright © 2016 Kovilant Ltd. | All rights reserved</p>
  </div>
</footer>

</body>
</html>
```